Ice cream packages for CASA MORELLANO

We need a design for ice cream packaging for premium market. Size of the pack 16 oz and 32 oz conic design with cap. Has to be a generic design for all sour flavors, the distinction of the flavors will be don on the stores when people choose the flavor they want and we will place a label of the flavor they close, the design has to be including an area to put the label with the flavor

Target Market(s)

Premium Italian gelato ice cream markets

Industry/Entity Type

Deserts

Font styles to use
Other font styles liked:
• Didot for the logo and brand,

Colors

Designer to choose colors to be used in the design.

Requirements
Must have
• Our design of logo, fonts, and style similar to images sent INCLUD THE FIORE DOLCETTI LOGO , in small size at the side of the container; logo included in the photos bellow
Nice to have
• It has to be an universal design for all flavors, and we need an aérea to place the flavor of the ice cream with a label , expample “chocolate”

```html
<!DOCTYPE html>
<html lang="en">
<head>
<meta charset="utf-8">
<title>Casa Morellano – Gelato Pint and Lid</title>
<link rel="stylesheet" href="https://fonts.googleapis.com/css2?family=Bodoni+Moda:wght@400;500&display=swap">
<style>
  :root {
    --page-bg: #f8f8f8;
    --cup-white: #ffffff;
    --cup-shade: #cfcfcf;
    --band-black: #111111;
    --band-brown: #6b5440;
    --band-sheen: #8a8580;
    --lid-brown: #67523f;
    --lid-ring: #1d1712;
    --ink-brown: #3e3128;
    --text-light: #f4f1ec;
    --ornament-dark: #1e1915;
    --ornament-brown: #5e4a39;
  }
  html, body {
    margin: 0;
    padding: 0;
    width: 1200px;
    height: 750px;
    overflow: hidden;
    background: var(--page-bg);
  }
  .packaging {
    display: block;
    width: 1200px;
    height: 750px;
  }
  .brand-type {
    font-family: "Bodoni Moda", "Didot", serif;
    font-weight: 400;
  }
  .flavour-type {
    font-family: "Bodoni Moda", "Didot", serif;
    font-weight: 500;
  }
</style>
</head>
<body>
<svg class="packaging" viewBox="0 0 1200 750" xmlns="http://www.w3.org/2000/svg">
  <defs>
    <linearGradient id="band-metal" x1="0" x2="1" y1="0" y2="0">
      <stop offset="0" stop-color="var(--band-black)"/>
      <stop offset="0.3" stop-color="var(--band-black)"/>
      <stop offset="0.5" stop-color="var(--band-brown)"/>
      <stop offset="0.7" stop-color="var(--band-black)"/>
      <stop offset="1" stop-color="var(--band-black)"/>
    </linearGradient>
    <linearGradient id="label-metal" x1="0" x2="1" y1="0" y2="0">
      <stop offset="0" stop-color="var(--band-black)"/>
      <stop offset="0.3" stop-color="var(--band-black)"/>
      <stop offset="0.45" stop-color="var(--band-brown)"/>
      <stop offset="0.62" stop-color="var(--band-black)"/>
      <stop offset="0.85" stop-color="var(--band-sheen)"/>
      <stop offset="1" stop-color="var(--band-black)"/>
    </linearGradient>
    <linearGradient id="cup-body-shade" x1="0" x2="1" y1="0" y2="0">
      <stop offset="0" stop-color="var(--cup-shade)"/>
      <stop offset="0.12" stop-color="var(--cup-white)"/>
      <stop offset="0.8" stop-color="var(--cup-white)"/>
      <stop offset="1" stop-color="var(--cup-shade)"/>
    </linearGradient>
    <linearGradient id="ornament-tone" x1="0" x2="1" y1="0" y2="0">
      <stop offset="0" stop-color="var(--ornament-dark)"/>
      <stop offset="0.45" stop-color="var(--ornament-brown)"/>
      <stop offset="0.75" stop-color="var(--ornament-dark)"/>
      <stop offset="1" stop-color="var(--ornament-brown)"/>
    </linearGradient>
    <linearGradient id="ornament-fade" x1="0" x2="0" y1="0" y2="1">
      <stop offset="0" stop-color="#fff" stop-opacity="0.35"/>
      <stop offset="0.6" stop-color="#fff" stop-opacity="0.1"/>
      <stop offset="1" stop-color="#fff" stop-opacity="0"/>
    </linearGradient>
    <clipPath id="cup-body-clip">
      <path d="M284 266 L567 266 L551 548 Q426 553 301 548 Z"/>
    </clipPath>
  </defs>

  <!-- pint container -->
  <g class="pint">
    <path class="pint-body" d="M284 266 L567 266 L551 548 Q426 553 301 548 Z" fill="url(#cup-body-shade)"/>

    <g class="pint-ornament-area" clip-path="url(#cup-body-clip)" role="img" aria-label="Decorative black and brown scroll pattern across the upper part of the cup">
      <path d="M280 266 L572 266 L572 372 Q540 390 505 376 Q470 362 440 352 Q400 340 372 370 Q345 392 305 375 L280 368 Z" fill="url(#ornament-tone)" opacity="0.82"/>
      <path d="M280 266 L572 266 L572 372 Q540 390 505 376 Q470 362 440 352 Q400 340 372 370 Q345 392 305 375 L280 368 Z" fill="url(#ornament-fade)"/>
    </g>

    <g class="pint-brand">
      <circle cx="426" cy="412" r="9" fill="var(--ink-brown)"/>
      <text class="brand-type" x="426" y="470" text-anchor="middle" font-size="26" fill="var(--ink-brown)">Casa Morellano</text>
    </g>

    <g class="flavour-label">
      <path d="M298 489 L553 489 L552 518 L299 518 Z" fill="url(#label-metal)"/>
      <text class="flavour-type" x="428" y="513" text-anchor="middle" font-size="22" fill="var(--text-light)">Chocolate</text>
    </g>

    <g class="pint-rim">
      <rect x="270" y="209" width="311" height="57" fill="url(#band-metal)"/>
      <text class="brand-type" x="338" y="245" text-anchor="middle" font-size="16" fill="var(--text-light)">Casa Morellano</text>
      <circle cx="424" cy="239" r="6" fill="var(--text-light)"/>
      <text class="brand-type" x="511" y="245" text-anchor="middle" font-size="16" fill="var(--text-light)">Casa Morellano</text>
    </g>
  </g>

  <!-- lid seen from above -->
  <g class="lid">
    <circle cx="754" cy="396" r="160" fill="var(--lid-brown)"/>
    <circle cx="754" cy="396" r="156" fill="none" stroke="var(--lid-ring)" stroke-width="2"/>
    <circle cx="754" cy="376" r="10" fill="var(--text-light)"/>
    <text class="brand-type" x="754" y="438" text-anchor="middle" font-size="28" fill="var(--text-light)">Casa Morellano</text>
  </g>
</svg>
</body>
</html>
```